依頼詳細
販売商品は下記の3種類です。詳細はURLをご参照下さい。

1.工業用精製水 (用途:実験室などでの試験器具洗浄など)
http://www.hanabo-tenko.com/shop/goods/goods/goods.php?act=Goods&mode=Detail&id=00054986

2.バッテリー補充液 (用途:バッテリーの補充液など)
http://www.hanabo-tenko.com/shop/goods/goods/goods.php?act=Goods&mode=Detail&id=00054987

3.高純度精製水 (用途:エステスチーマーや加湿器の補給水など)
http://www.hanabo-tenko.com/shop/goods/goods/goods.php?act=Goods&mode=Detail&id=00066908

精製水は純度の高い水(きれいな水)ですので、商品に相応しい爽やかな印象を持っていただけるデザインを希望します。全体的にブルー系統のカラーを希望します。

添付の原案のレイアウト通りの必要はありません。見やすく目的に沿った内容であれば、画像等の追加、文章やフレーズ、フォント、文字サイズなどの修正、加筆もOKです。基本的にはデザインを重視したいと思います。

記載事項が多いので、A4サイズに収まるレイアウトの工夫をお願い致します。
記載項目
添付の【原案】をご参照下さい。
サイズ
A4
ページ数
両面
希望イメージ
シンプル 複雑
単色 カラフル
暗い 明るい
日常 高級
遊び心 厳粛
未来的 伝統的
女性的 男性的
希望する色
水色系
納品ファイル
• 高解像度JPG (.jpg)
• イラストレーター形式 (.ai)
補足説明

当社の要望・イメージに最も近いデザインでした。

みなさん非常に素晴らしいご提案でしたので、選定に苦慮いたしました。

選定できなかった皆様には申し訳ございませんでしたが、またの機会がございましたらよろしくお願い致します。皆様のご尽力にとても感謝致します。

この度は誠にありがとうございました。

```html
<!DOCTYPE html>
<html lang="ja">
<head>
<meta charset="utf-8">
<title>精製水のご案内</title>
<link rel="stylesheet" href="https://fonts.googleapis.com/css2?family=Noto+Sans+JP:wght@400;700;900&family=M+PLUS+Rounded+1c:wght@700;800&display=swap">
<style>
:root{
  --blue:#1a7fd0;
  --deep:#0b4f9c;
  --sky:#cfeefd;
  --aqua:#58c3ee;
  --pale:#eef9ff;
  --orange:#f08c14;
  --red:#e2352b;
  --green:#3aa635;
  --ink:#2a3440;
  --white:#fff;
}
*{box-sizing:border-box;margin:0;padding:0}
html,body{width:849px;height:1200px;overflow:hidden;background:#fff}
body{font-family:"Noto Sans JP",sans-serif;color:var(--ink)}
.sheet{position:relative;width:849px;height:1200px;overflow:hidden;
  background:linear-gradient(180deg,#e4f6fe 0%,#bfe6fa 35%,#d9f2fd 60%,#eaf8ff 100%)}
.water-bg{position:absolute;left:0;top:30px;width:849px;height:420px;
  background:radial-gradient(ellipse at 30% 40%,#ffffffaa 0%,#ffffff00 50%),linear-gradient(160deg,#a9dcf6,#e8f7ff)}
.topbar{position:absolute;top:0;left:0;width:100%;height:30px;background:#fff;display:flex;align-items:center;padding:0 18px;font-size:12px}
.topbar .co{font-weight:700}
.topbar .url{margin-left:240px;font-size:11px;color:#555}
.topbar .tag{margin-left:auto;border:1px solid #999;font-size:9px;padding:2px 6px}
.title{position:absolute;left:210px;top:72px;width:420px;height:70px;background:#fffffff0;border-radius:35px;
  display:flex;align-items:center;justify-content:center;font-family:"M PLUS Rounded 1c",sans-serif;
  font-size:46px;font-weight:800;color:var(--blue);letter-spacing:2px;box-shadow:0 2px 8px #5ab0e055}
.badge{position:absolute;left:690px;top:40px;width:140px;height:140px;border-radius:50%;background:#fff;
  border:4px solid var(--aqua);text-align:center;padding-top:24px;color:var(--orange)}
.badge .tx{font-size:11px;color:var(--blue);font-weight:700}
.badge .pr{font-family:"M PLUS Rounded 1c",sans-serif;font-size:44px;font-weight:800;line-height:1}
.badge .pr small{font-size:16px}
.points{position:absolute;top:175px;left:40px;width:770px;display:flex;gap:14px}
.point{flex:1;background:#ffffffe6;border-radius:8px;padding:8px 10px;display:flex;gap:8px;font-size:11px;line-height:1.5}
.point .num{flex:none;width:34px;height:34px;border-radius:50%;background:var(--red);color:#fff;font-weight:900;
  display:flex;align-items:center;justify-content:center;font-size:18px}
.products{position:absolute;top:235px;left:40px;width:770px;display:flex;gap:20px}
.product{flex:1;text-align:center}
.product .name{display:flex;gap:6px;align-items:center;justify-content:center}
.product .label{background:var(--deep);color:#fff;font-weight:700;font-size:14px;padding:4px 8px;border-radius:4px}
.product .code{display:block;font-size:9px;opacity:.8}
.product .chip{background:var(--green);color:#fff;font-size:10px;padding:3px 5px;border-radius:4px;line-height:1.2}
.product .pic{margin-top:8px;height:150px;border-radius:6px;background:linear-gradient(160deg,#ffffff,#cde9f8 60%,#9fd2ef)}
.product .use{margin-top:6px;font-size:10px;color:var(--deep);font-weight:700}
.feature{position:absolute;top:470px;left:40px;width:770px;background:#fff;border-radius:10px;border:2px solid var(--aqua);
  padding:14px 14px 14px 110px;font-size:12px;line-height:1.8}
.feature .mark{position:absolute;left:18px;top:22px;width:72px;height:72px;border-radius:50%;background:var(--orange);
  color:#fff;font-weight:900;font-size:20px;display:flex;align-items:center;justify-content:center}
.spec{position:absolute;top:600px;left:40px;width:770px;font-size:11px;line-height:1.7;color:#333}
.bulk{position:absolute;top:650px;left:190px;width:470px;height:40px;background:var(--blue);border-radius:20px;color:#fff;
  font-family:"M PLUS Rounded 1c",sans-serif;font-size:24px;font-weight:800;display:flex;align-items:center;justify-content:center}
.bulk em{font-style:normal;color:#ffe45a}
.contact{position:absolute;top:700px;left:40px;width:770px;background:#fff;border-radius:8px;height:70px;display:flex;align-items:center;padding:0 14px;gap:18px}
.contact .head{background:var(--deep);color:#fff;font-size:12px;font-weight:700;padding:6px 8px;border-radius:4px}
.contact .tel{font-weight:900;font-size:18px;color:var(--deep);display:flex;align-items:center;gap:4px}
.contact .tel small{font-size:9px;font-weight:400;display:block;color:#555}
.contact .mail{font-size:12px;font-weight:700;color:var(--deep)}
.contact .shop{margin-left:auto;font-size:14px;font-weight:700;color:var(--blue);display:flex;align-items:center;gap:6px}
.contact .shop i{width:12px;height:12px;background:var(--blue);display:inline-block}
.oem{position:absolute;top:790px;left:40px;width:770px}
.oem h2{font-family:"M PLUS Rounded 1c",sans-serif;font-size:24px;font-weight:800;color:var(--deep);text-align:center}
.oem h2 em{font-style:normal;color:var(--orange)}
.oem .row{display:flex;gap:12px;margin-top:14px}
.oem .box{background:#fff;border-radius:8px;padding:10px;font-size:11px;line-height:1.6;display:flex;gap:8px;align-items:center}
.oem .box b{flex:none;background:var(--aqua);color:#fff;border-radius:6px;padding:6px;font-size:12px;text-align:center;line-height:1.3}
.oem .ask{flex:none;width:120px;background:var(--orange);color:#fff;border-radius:50%;height:120px;text-align:center;font-weight:700;font-size:13px;display:flex;align-items:center;justify-content:center;line-height:1.4}
.footer{position:absolute;bottom:0;left:0;width:100%;height:90px;background:#fff}
.footer .info{display:flex;align-items:center;gap:14px;font-size:10px;padding:10px 18px}
.footer .info .co{font-weight:900;font-size:13px}
.footer .info .tel{font-weight:700;font-size:13px}
.footer .fax{margin:4px 18px;background:var(--deep);color:#fff;font-size:15px;font-weight:700;padding:8px 14px;border-radius:4px}
.footer .fax em{font-style:normal;color:#ffe45a}
</style>
</head>
<body>
<div class="sheet">
  <div class="water-bg" role="img" aria-label="水しぶきと泡の背景写真"></div>
  <header class="topbar">
    <span class="co">株式会社 花房</span>
    <span class="url">www.hanabo-tenko.com</span>
    <span class="tag">水処理用品 総合案内</span>
  </header>

  <h1 class="title">精製水のご案内</h1>
  <div class="badge">
    <div class="tx">Purified Water</div>
    <div class="pr">945<small>円から</small></div>
    <div class="tx">（税込）</div>
  </div>

  <section class="points">
    <div class="point"><span class="num">1</span><p>自社製造・直販だからこそ実現できる納得の価格です。</p></div>
    <div class="point"><span class="num">2</span><p>16時までのご注文は当日出荷！16時以降は翌営業日の発送です。</p></div>
    <div class="point"><span class="num">3</span><p>用途に応じて選べる3種類の精製水をご用意しております。</p></div>
  </section>

  <section class="products">
    <div class="product">
      <div class="name"><span class="label">工業用精製水<span class="code">TSP-01</span></span><span class="chip">除菌<br>フィルター</span></div>
      <div class="pic" role="img" aria-label="工業用精製水の箱入りパッケージ写真"></div>
      <p class="use">ボイラー用水や実験器具の洗浄に</p>
    </div>
    <div class="product">
      <div class="name"><span class="label">バッテリー補充液<span class="code">TSP-02</span></span><span class="chip">除菌<br>フィルター</span></div>
      <div class="pic" role="img" aria-label="バッテリー補充液の箱入りパッケージ写真"></div>
      <p class="use">自動車・フォークリフトのバッテリーに</p>
    </div>
    <div class="product">
      <div class="name"><span class="label">高純度精製水<span class="code">TSP-03</span></span><span class="chip">紫外線<br>殺菌処理</span></div>
      <div class="pic" role="img" aria-label="高純度精製水の箱入りパッケージ写真"></div>
      <p class="use">スチーマーや加湿器の補給水に</p>
    </div>
  </section>

  <section class="feature">
    <span class="mark">特徴</span>
    <p>逆浸透膜及びイオン交換樹脂を使用し、限りなくイオン成分を取り除いています。<br>
    活性炭・除菌フィルター及び紫外線殺菌装置を使用し、衛生的に製造しています。<br>
    持ち運びやすい取っ手付きです。（付属の専用コックは別売です）</p>
  </section>

  <p class="spec">●容量：20L　●サイズ：300×300×300mm　●電気伝導率：1.0μS/cm以下　●梱包：段ボール箱入り</p>

  <div class="bulk">まとめ買いでさらに<em>お得</em>に！</div>

  <section class="contact">
    <span class="head">ご注文・お問合せ</span>
    <span class="tel"><svg width="16" height="16" viewBox="0 0 24 24"><path fill="#0b4f9c" d="M6.6 10.8a15 15 0 0 0 6.6 6.6l2.2-2.2c.3-.3.7-.4 1-.2 1.1.4 2.3.6 3.6.6.6 0 1 .4 1 1V20c0 .6-.4 1-1 1A17 17 0 0 1 3 4c0-.6.4-1 1-1h3.5c.6 0 1 .4 1 1 0 1.3.2 2.5.6 3.6.1.3 0 .7-.2 1z"/></svg><span>0120-555-201<small>TEL 受付 9:00〜17:00</small></span></span>
    <span class="tel"><span>0120-555-202<small>FAX 24時間受付</small></span></span>
    <span class="mail">sales@hanabo-tenko.com</span>
    <span class="shop"><i></i>清水用品.com</span>
  </section>

  <section class="oem">
    <h2>弊社オリジナルの<em>精製水</em>をご販売されませんか？</h2>
    <div class="row">
      <div class="box"><b>小ロットで<br>OEM製造</b><p>オリジナルラベルでの製造を小ロットから承ります。</p></div>
      <div class="box"><b>在庫リスク<br>なし！</b><p>ご注文ごとに直送するため在庫を持つ必要がありません。</p></div>
      <div class="ask">ご相談は<br>お電話または<br>Eメールで</div>
    </div>
  </section>

  <footer class="footer">
    <div class="info">
      <span class="co">株式会社 花房</span>
      <span>〒900-0001 架空県青葉郡水辺町1-2-3</span>
      <span class="tel">TEL 0900(12)3401</span>
      <span class="tel">FAX 0900(12)3402</span>
    </div>
    <div class="fax">FAXでのご注文は、裏面の<em>【注文シート（FAX専用）】</em>をご利用下さい。</div>
  </footer>
</div>
</body>
</html>
```